Graphic Design for Labels

I'm needing a label for my skincare line based in Vancouver, BC. The name of the company is 'Velvet Dawn Skincare' and the tag line is 'Stay Kind to Your Face'. It should indicate somewhere on the lable that it is made with raw fireweed honey.
There are two products the first is Moisturizing Face Cream and second is Nourishing Face Buff. I would like some honey-comb incorporated around the edges of the label and a black and white detailed honeybee somewhere on the label, maybe looking like it was hand drawn with a fine tip black marker or pencil. It will need to have the amount of product in the front which is 120 ml.
I'm open to different colours but nothing too bright, I want a delicate feel to the colours. Overall I would like the label to have a boutiquey artisan feel. I will also require an ingredient label for the back of the bottles the exact same size as the front label with the company info there as well. And some directions. The ingredients and directions can read whatever for now and I will provide those details when I'm ready to order the labels if that's possible, if not let me know asap and I can provide the details. After the ingredients list I would like it to read:
'Paraben and Sulfate free'
At the bottom of the back label I would like it to read:
'Please Recycle'
and then the company name and location at the very bottom
Updates
I like the way this label is organized, and especially how the company name is in the circle around the butterfly. Maybe that could be done with a honey bee and if the Net Weight could be included like it is on this bottle that would be great - 4 oz (115g)
The flowers are nice, but maybe it would look good to have simlpe hand drawn flowers with a bee flying around, if possible?

```html
<!DOCTYPE html>
<html lang="en">
<head>
<meta charset="utf-8">
<title>Velvet Dawn Skincare – Moisturizing Face Cream Label</title>
<link rel="stylesheet" href="https://fonts.googleapis.com/css2?family=Cormorant+Garamond:ital,wght@1,600&family=Marcellus&family=Raleway:wght@500;700&family=Jura:wght@600&display=swap">
<style>
  :root {
    --frame: #4a4440;
    --bg-light: #f8efea;
    --bg-mid: #ebcdb9;
    --bg-edge: #d9a686;
    --brand: #b9764f;
    --rule: #c98e6a;
    --ink: #5a3a26;
    --cream-hi: #b27a52;
    --cream-lo: #6e4326;
    --cream-stroke: #7a5220;
    --comb-light: #f1e8dc;
    --comb-grey: #d9d2c8;
    --comb-amber: #c8913f;
    --comb-deep: #9c6426;
    --comb-edge: #f6d98a;
    --ornament: #5a3620;
  }
  * { margin: 0; padding: 0; box-sizing: border-box; }
  html, body { width: 973px; height: 1200px; overflow: hidden; background: #fff; }
  .label {
    position: relative;
    width: 973px;
    height: 1200px;
    border: 3px solid var(--frame);
    background: radial-gradient(ellipse 70% 60% at 48% 45%, var(--bg-light) 0%, var(--bg-mid) 60%, var(--bg-edge) 100%);
    overflow: hidden;
  }
  .decor { position: absolute; inset: -3px; }
  .brand-mark {
    position: absolute;
    left: 383px; top: 62px;
    width: 210px; height: 210px;
    border: 7px solid var(--brand);
    border-radius: 50%;
  }
  .brand {
    position: absolute;
    left: 0; right: 0; top: 268px;
    text-align: center;
    color: var(--brand);
  }
  .brand-name {
    display: block;
    font-family: "Marcellus", serif;
    font-size: 84px;
    line-height: 1;
  }
  .brand-sub {
    display: block;
    font-family: "Raleway", sans-serif;
    font-weight: 700;
    font-size: 26px;
    letter-spacing: 17px;
    padding-left: 17px;
    margin-top: 14px;
  }
  .rule {
    position: absolute;
    left: 170px; width: 631px; top: 398px;
    height: 2px; background: var(--rule);
  }
  .product-note {
    position: absolute;
    left: 380px; right: 40px; top: 442px;
    text-align: center;
    font-family: "Raleway", sans-serif;
    font-weight: 700;
    font-size: 20px;
    letter-spacing: 2px;
    color: var(--brand);
  }
  .product-type {
    position: absolute;
    left: 0; right: 0; top: 535px;
    text-align: center;
    font-family: "Raleway", sans-serif;
    font-weight: 500;
    font-size: 58px;
    line-height: 1;
    letter-spacing: 3px;
    color: var(--ink);
  }
  .product-name {
    position: absolute;
    left: 0; right: 0; top: 580px;
    text-align: center;
    font-family: "Cormorant Garamond", serif;
    font-style: italic;
    font-weight: 600;
    font-size: 212px;
    line-height: 1;
    background: linear-gradient(180deg, var(--cream-hi), var(--cream-lo));
    -webkit-background-clip: text;
    background-clip: text;
    color: transparent;
    -webkit-text-stroke: 2px var(--cream-stroke);
  }
  .tagline {
    position: absolute;
    left: 0; right: 0; top: 965px;
    text-align: center;
    font-family: "Jura", sans-serif;
    font-weight: 600;
    font-size: 92px;
    line-height: 105px;
    color: var(--ornament);
  }
</style>
</head>
<body>
<main class="label">
  <svg class="decor" width="973" height="1200" viewBox="0 0 973 1200" xmlns="http://www.w3.org/2000/svg">
    <defs>
      <linearGradient id="combLeft" x1="0" y1="0" x2="1" y2="1">
        <stop offset="0" stop-color="var(--comb-amber)"/>
        <stop offset="0.45" stop-color="var(--comb-light)"/>
        <stop offset="0.75" stop-color="var(--comb-grey)"/>
        <stop offset="1" stop-color="var(--comb-amber)"/>
      </linearGradient>
      <linearGradient id="combRight" x1="0" y1="0" x2="1" y2="1">
        <stop offset="0" stop-color="var(--comb-deep)"/>
        <stop offset="1" stop-color="var(--comb-amber)"/>
      </linearGradient>
    </defs>
    <polygon role="img" aria-label="Honeycomb cells spreading from the left edge toward the centre"
             points="0,485 138,490 185,430 336,433 364,518 336,595 430,639 600,705 626,821 595,915 518,992 397,997 364,1058 331,1141 298,1203 0,1203"
             fill="url(#combLeft)" stroke="var(--comb-edge)" stroke-width="7" stroke-linejoin="round" opacity="0.9"/>
    <polygon role="img" aria-label="Honeycomb cells in the lower right corner"
             points="501,1203 518,1091 584,1036 678,1041 705,986 837,970 882,1058 870,1113 882,1203"
             fill="url(#combRight)" stroke="var(--comb-edge)" stroke-width="7" stroke-linejoin="round" opacity="0.9"/>
    <rect role="img" aria-label="Curling scroll ornament on the left" x="28" y="962" width="180" height="198" rx="50" fill="var(--ornament)" opacity="0.3"/>
    <rect role="img" aria-label="Curling scroll ornament on the right" x="762" y="962" width="186" height="198" rx="50" fill="var(--ornament)" opacity="0.3"/>
  </svg>

  <span class="brand-mark" aria-hidden="true"></span>
  <header class="brand">
    <span class="brand-name">Velvet Dawn</span>
    <span class="brand-sub">Skincare</span>
  </header>
  <div class="rule"></div>

  <p class="product-note">Raw Fireweed Honey · 120 ml</p>
  <p class="product-type">Moisturizing</p>
  <h1 class="product-name">Face Cream</h1>

  <p class="tagline">Stay Kind<br>to Your Face</p>
</main>
</body>
</html>
```